Wild Ridge Trekcraft DL flyer

I'm looking for a new flyer for my startup business. In Darwin Australia.
Aimed at family's and short stay tourists the "Wild Ridge Trekcraft" 4 hr tour will give people a basic understanding of some essential bush survival skills in the Australian Outback.
things covered in this 4 hr tour are
1. Finding water.
2. finding food.
3. Finding/making shelter and fire.
4. Finding your way home.

The tour will pick clients up in an air conditioned purpose build 4WD and take them to a nearby bushland area where they will have the opportunity to catch and harvest some native bushtucker.
They will then be able to find/harvest some water for survival situations.
While we cook our bush tucker they will also learn to find their way home through ancient navigation techniques as well.

Clients will then be dropped back to their accomodation with some fun and vital knowledge of surviving in the Australian outback.
At the end of the tour the group will be able to take home a basic survival kit which they will be able to use through the skills they just gained on the tour.

I'd like a two sided DL size flyer emphasising the following points.
4hr/half day tour
Fun for the family
Free survival kit included.
Eat what you catch
Learn essential survival skills
Provided buy an experienced and passionate bushman.
$150/head including transfers.

I'll provide some pictures for the flyer and any extra content you require.
Updates

Target Market(s)

Family's
Short stay tourists

Industry/Entity Type

Tourism

Colors

Designer to choose colors to be used in the design.

Requirements
Must have
• As per brief
Nice to have
• Any extra content and flair designers would like to add
Should not have
• Any images which aren't Australian

```html
<!DOCTYPE html>
<html lang="en">
<head>
<meta charset="utf-8">
<title>Wild Ridge Trekcraft DL flyer</title>
<link rel="stylesheet" href="https://fonts.googleapis.com/css2?family=Cinzel:wght@600;700&family=Crimson+Text:wght@400;600;700&family=Share+Tech+Mono&display=swap">
<style>
  :root {
    --page-bg: #e9e6e1;
    --parchment-light: #fbf1dc;
    --parchment-mid: #f2dfb6;
    --parchment-edge: #e5c994;
    --olive: #939a35;
    --olive-dark: #6b6a2c;
    --ink: #1f1a14;
    --accent-orange: #ea5a24;
    --white: #ffffff;
    --photo-earth: #6e5a44;
    --photo-bush: #7f8f4a;
  }
  * { box-sizing: border-box; margin: 0; padding: 0; }
  html, body { width: 1127px; height: 1200px; overflow: hidden; background: var(--page-bg); }
  .canvas { position: relative; width: 1127px; height: 1200px; }

  .flyer {
    position: absolute; width: 434px; height: 911px; overflow: hidden;
    background: radial-gradient(ellipse at 50% 45%, var(--parchment-light) 0%, var(--parchment-mid) 65%, var(--parchment-edge) 100%);
    box-shadow: 0 6px 18px rgba(0,0,0,0.25);
  }
  .flyer--front { left: 88px; top: 79px; }
  .flyer--back { left: 601px; top: 179px; }

  .hero { position: absolute; left: 0; top: 0; width: 434px; }
  .inset-photo {
    position: absolute; border: 5px solid var(--white);
    box-shadow: 0 3px 8px rgba(0,0,0,0.35);
  }
  .inset-photo--round { border-radius: 50%; border-width: 6px; }

  .title { position: absolute; right: 20px; font-family: "Cinzel", serif; font-weight: 700; text-align: right; line-height: 1; }
  .title__small { top: 362px; font-size: 40px; color: var(--olive-dark); }
  .title__large { top: 418px; font-size: 50px; color: var(--ink); letter-spacing: 0.5px; }
  .title__large span { color: var(--olive-dark); }
  .title-rule { position: absolute; left: 26px; right: 20px; top: 482px; height: 1px; background: var(--olive-dark); }

  .mono { font-family: "Share Tech Mono", monospace; color: var(--accent-orange); }
  .tagline { position: absolute; left: 10px; right: 10px; top: 502px; text-align: center; font-size: 18px; letter-spacing: 2px; line-height: 1.35; }

  .checklist { position: absolute; left: 22px; top: 606px; list-style: none; font-family: "Crimson Text", serif; font-size: 18px; color: var(--ink); }
  .checklist li { display: flex; align-items: center; height: 29px; }
  .checklist svg { width: 20px; height: 20px; margin-right: 10px; flex: none; }

  .price { position: absolute; font-size: 15px; letter-spacing: 1px; }
  .flyer--front .price { left: 52px; top: 785px; }
  .flyer--back .price { left: 16px; top: 752px; width: 230px; text-align: center; line-height: 1.4; }

  .footer-band { position: absolute; left: 0; bottom: 0; width: 434px; }
  .footer-text { position: absolute; left: 0; right: 0; text-align: center; color: var(--white); }
  .book-now { font-family: "Crimson Text", serif; font-weight: 700; font-size: 22px; }
  .web { font-family: "Share Tech Mono", monospace; font-size: 19px; letter-spacing: 1.5px; }
  .flyer--front .book-now { top: 842px; }
  .flyer--front .web { top: 872px; }
  .flyer--back .book-now { top: 842px; }
  .flyer--back .web { top: 872px; }

  .headline { position: absolute; left: 0; right: 0; top: 178px; text-align: center; font-family: "Cinzel", serif; font-weight: 700; font-size: 43px; line-height: 1.05; color: var(--white); text-shadow: 0 2px 4px rgba(0,0,0,0.45); }
  .intro { position: absolute; left: 24px; right: 24px; top: 352px; text-align: center; font-family: "Crimson Text", serif; font-size: 17.5px; line-height: 1.3; color: var(--accent-orange); }
  .steps { position: absolute; left: 22px; top: 512px; list-style: none; font-family: "Crimson Text", serif; font-size: 19px; color: var(--ink); }
  .steps li { display: flex; line-height: 1.2; margin-bottom: 14px; max-width: 220px; }
  .steps b { color: var(--olive-dark); font-size: 23px; width: 24px; flex: none; line-height: 1; }
</style>
</head>
<body>
<div class="canvas">

  <!-- Front side -->
  <section class="flyer flyer--front">
    <svg class="hero" width="434" height="340" viewBox="0 0 434 340">
      <defs>
        <linearGradient id="front-photo" x1="0" y1="0" x2="1" y2="1">
          <stop offset="0" stop-color="#5b4a3a"/><stop offset="0.5" stop-color="#7c8a6a"/><stop offset="1" stop-color="#3e3429"/>
        </linearGradient>
      </defs>
      <path d="M0 0 H434 V300 Q260 345 0 268 Z" fill="url(#front-photo)" role="img" aria-label="Photo of a freshwater crayfish held in open hands"/>
      <path d="M0 268 Q260 345 434 300" fill="none" stroke="var(--white)" stroke-width="7"/>
    </svg>
    <div class="inset-photo inset-photo--round" style="left:16px;top:262px;width:152px;height:152px;background:radial-gradient(circle at 50% 55%, #8a9a4a, #c9a88f);" role="img" aria-label="Photo of spiky green bush fruit held in a palm"></div>

    <div class="title title__small">WILD RIDGE</div>
    <div class="title title__large">TREK<span>CRAFT</span></div>
    <div class="title-rule"></div>

    <p class="tagline mono">Provided buy an experienced and passionate bushman.</p>

    <ul class="checklist">
      <li><svg viewBox="0 0 20 20"><rect x="2" y="5" width="13" height="13" fill="none" stroke="var(--olive-dark)" stroke-width="2"/><path d="M5 11 L9 15 L18 3" fill="none" stroke="var(--olive-dark)" stroke-width="2.5"/></svg>4hr/half day tour.</li>
      <li><svg viewBox="0 0 20 20"><rect x="2" y="5" width="13" height="13" fill="none" stroke="var(--olive-dark)" stroke-width="2"/><path d="M5 11 L9 15 L18 3" fill="none" stroke="var(--olive-dark)" stroke-width="2.5"/></svg>Free survival kit included.</li>
      <li><svg viewBox="0 0 20 20"><rect x="2" y="5" width="13" height="13" fill="none" stroke="var(--olive-dark)" stroke-width="2"/><path d="M5 11 L9 15 L18 3" fill="none" stroke="var(--olive-dark)" stroke-width="2.5"/></svg>Fun for the family!</li>
      <li><svg viewBox="0 0 20 20"><rect x="2" y="5" width="13" height="13" fill="none" stroke="var(--olive-dark)" stroke-width="2"/><path d="M5 11 L9 15 L18 3" fill="none" stroke="var(--olive-dark)" stroke-width="2.5"/></svg>Eat what you catch!</li>
      <li><svg viewBox="0 0 20 20"><rect x="2" y="5" width="13" height="13" fill="none" stroke="var(--olive-dark)" stroke-width="2"/><path d="M5 11 L9 15 L18 3" fill="none" stroke="var(--olive-dark)" stroke-width="2.5"/></svg>Learn essential survival skills!</li>
    </ul>

    <div class="inset-photo" style="left:262px;top:612px;width:160px;height:128px;transform:rotate(10deg);background:linear-gradient(135deg,#4f6a3a,#a8b87a 55%,#3c4a2c);" role="img" aria-label="Photo of pandanus palm leaves"></div>

    <p class="price mono">$150/head including transfers.</p>

    <svg class="footer-band" width="434" height="92" viewBox="0 0 434 92">
      <path d="M0 10 L20 6 L38 11 L60 4 L84 9 L110 5 L140 10 L170 3 L200 8 L232 5 L262 10 L290 4 L320 9 L352 6 L380 11 L408 5 L434 9 V92 H0 Z" fill="var(--white)"/>
      <path d="M0 15 L24 11 L46 16 L70 10 L96 14 L124 9 L150 15 L182 9 L212 13 L240 10 L270 15 L300 9 L330 14 L360 11 L390 16 L414 10 L434 14 V92 H0 Z" fill="var(--olive)"/>
    </svg>
    <div class="footer-text book-now">BOOK NOW</div>
    <div class="footer-text web">www.WildRidgeTrekcraft.au</div>
  </section>

  <!-- Back side -->
  <section class="flyer flyer--back">
    <svg class="hero" width="434" height="340" viewBox="0 0 434 340">
      <defs>
        <linearGradient id="back-photo" x1="0" y1="0" x2="0" y2="1">
          <stop offset="0" stop-color="#9fb09a"/><stop offset="0.45" stop-color="#6f7d45"/><stop offset="0.7" stop-color="#9b5a2e"/><stop offset="1" stop-color="#6f8a3a"/>
        </linearGradient>
      </defs>
      <rect x="0" y="0" width="434" height="60" fill="var(--olive)"/>
      <path d="M0 46 L22 50 L48 44 L76 49 L104 43 L130 48 L160 44 L188 50 L218 45 L248 49 L276 43 L306 48 L336 44 L364 50 L394 45 L434 48 V340 H0 Z" fill="var(--white)"/>
      <path d="M0 52 L26 56 L52 50 L80 55 L108 49 L136 54 L164 50 L194 56 L222 51 L252 55 L282 49 L312 54 L340 50 L370 56 L400 51 L434 54 V258 Q300 335 0 305 Z" fill="url(#back-photo)" role="img" aria-label="Photo of outback woodland with termite mounds in tall grass"/>
      <path d="M0 305 Q300 335 434 258" fill="none" stroke="var(--white)" stroke-width="7"/>
    </svg>
    <h1 class="headline">EAT WHAT<br>YOU CATCH!</h1>

    <p class="intro">Aimed at family's and short stay tourists the "Wild Ridge Trekcraft" 4 hr tour will give people a basic understanding of some essential bush survival skills in the Australian Outback. things covered in this 4 hr tour are</p>

    <ol class="steps">
      <li><b>1.</b>Finding water</li>
      <li><b>2.</b>Finding food</li>
      <li><b>3.</b>Finding/making shelter and fire.</li>
      <li><b>4.</b>Finding your way home</li>
    </ol>

    <div class="inset-photo" style="left:272px;top:495px;width:165px;height:120px;transform:rotate(12deg);background:linear-gradient(135deg,#a88a66,#c9b08a 60%,#8e7355);" role="img" aria-label="Photo of sticks on the ground marking east and west"></div>
    <div class="inset-photo" style="left:246px;top:620px;width:170px;height:130px;transform:rotate(-10deg);background:linear-gradient(135deg,#6e8a5a,#9a8a6a 55%,#4f5e3a);" role="img" aria-label="Photo of the bushman guide in a wide-brim hat"></div>

    <p class="price mono">$150/head including transfers.</p>

    <svg class="footer-band" width="434" height="92" viewBox="0 0 434 92">
      <path d="M0 10 L20 6 L38 11 L60 4 L84 9 L110 5 L140 10 L170 3 L200 8 L232 5 L262 10 L290 4 L320 9 L352 6 L380 11 L408 5 L434 9 V92 H0 Z" fill="var(--white)"/>
      <path d="M0 15 L24 11 L46 16 L70 10 L96 14 L124 9 L150 15 L182 9 L212 13 L240 10 L270 15 L300 9 L330 14 L360 11 L390 16 L414 10 L434 14 V92 H0 Z" fill="var(--olive)"/>
    </svg>
    <div class="footer-text book-now">BOOK NOW</div>
    <div class="footer-text web">www.WildRidgeTrekcraft.au</div>
  </section>

</div>
</body>
</html>
```